Lantern's Pick CBD Packaging and Branding

We are looking for packaging designs for a new doctor focused CBD brand that is disease specific formulations (i.e. Bone and Joint Formula, Pelvic Formula, Pain Formula, Inflammation Formula, ect.) We would like the first packaging prototype to be our Pain Formulation. Our tagline is, "The Lantern's Pick" & we would also like the phrase, "Life. Balanced." - We are looking for our Logo to be on the box as well. We currently need a logo as well. We would like the letters "QX" to be more prominent than "vita" Our first product will be SoftGels and the active ingredient list can be made up at the moment. Our brand and packaging needs to convey authority, trust and scientific knowledge (since all of our formulations are created by researched and renowned doctors and scientists), but we also don't want to be too clinical feeling, so adding a modern touch. Attached are some sample designs for reference (none are the final iteration) as well as some vectorized art.

Target Market(s)

40-60 year old patients

Industry/Entity Type

Medical And Science

Logo Text

QX Vita

Requirements
Must have
• Clean, professional and trusting medical designs with a modern touch. New logo incorporated into the design.
Should not have
• Not too clinical feeling - Not pharmaceutical

```html
<!DOCTYPE html>
<html lang="en">
<head>
<meta charset="utf-8">
<title>QX Vita — SoftGels Pain Formulation Packaging</title>
<link rel="stylesheet" href="https://fonts.googleapis.com/css2?family=Open+Sans:ital,wght@0,400;0,600;0,700;1,400&family=Encode+Sans+Semi+Condensed:wght@400;600&family=Mrs+Saint+Delafield&display=swap">
<style>
  :root {
    --navy: #0c2a4a;
    --green: #26cd78;
    --grey: #7f8fa3;
    --fold: #e0393c;
    --cut: #2b2b2b;
    --paper: #ffffff;
  }
  html, body {
    margin: 0;
    width: 1200px;
    height: 720px;
    overflow: hidden;
    background: var(--paper);
  }
  .canvas { display: block; width: 1200px; height: 720px; }
  .sans { font-family: "Open Sans", sans-serif; }
  .italic { font-family: "Open Sans", sans-serif; font-style: italic; }
  .product { font-family: "Encode Sans Semi Condensed", sans-serif; letter-spacing: -2px; }
  .script { font-family: "Mrs Saint Delafield", cursive; }
  .brand-name { font-family: "Open Sans", sans-serif; font-weight: 600; fill: var(--navy); }
  .brand-tag { font-family: "Open Sans", sans-serif; fill: var(--grey); letter-spacing: 1px; }
  .cut-line { fill: none; stroke: var(--cut); stroke-width: 1.5; }
  .fold-line { stroke: var(--fold); stroke-width: 1.5; fill: none; }
  .rule { stroke: var(--green); stroke-width: 2; }
  .band { fill: var(--green); }
  .navy { fill: var(--navy); }
  .green { fill: var(--green); }
  .white { fill: #fff; }
  .grey { fill: var(--grey); }
</style>
</head>
<body>
<svg class="canvas" viewBox="0 0 2480 1488" xmlns="http://www.w3.org/2000/svg">

  <!-- Brand lockup -->
  <g class="brand-lockup">
    <text class="brand-name" x="172" y="790" font-size="112">QX Vita</text>
    <text class="brand-tag" x="172" y="852" font-size="36">the lantern’s pick</text>
  </g>

  <!-- Dieline: colour fills -->
  <g class="dieline-fills">
    <polygon class="band" points="1258,312 1275,312 1275,345 1528,345 1540,453 1818,453 1818,578 1258,578"/>
    <polygon class="band" points="656,905 1258,905 1258,1120 1254,1030 992,1030 987,1137 716,1137 705,1020 656,1010"/>
  </g>

  <!-- Dieline: cut lines -->
  <g class="dieline-cuts">
    <path class="cut-line" d="M716,470 L672,488 L672,997 L716,1013"/>
    <path class="cut-line" d="M716,470 L732,362 L970,362 L987,470"/>
    <path class="cut-line" d="M987,470 L987,198 L1258,198 L1258,470"/>
    <path class="cut-line" d="M993,198 Q993,155 1040,155 L1206,155 Q1252,155 1252,198"/>
    <path class="cut-line" d="M1258,470 L1273,362 L1515,362 L1530,470"/>
    <path class="cut-line" d="M1530,470 L1802,470 L1802,1284"/>
    <path class="cut-line" d="M716,1013 L732,1121 L970,1121 L987,1013"/>
    <path class="cut-line" d="M1258,1013 L1272,1121 L1515,1121 L1530,1013"/>
    <path class="cut-line" d="M1530,1013 L1530,1284"/>
    <path class="cut-line" d="M1536,1284 Q1536,1328 1582,1328 L1750,1328 Q1796,1328 1796,1284"/>
  </g>

  <!-- Dieline: fold lines -->
  <g class="dieline-folds">
    <line class="fold-line" x1="716" y1="470" x2="1530" y2="470"/>
    <line class="fold-line" x1="716" y1="1013" x2="1802" y2="1013"/>
    <line class="fold-line" x1="716" y1="470" x2="716" y2="1013"/>
    <line class="fold-line" x1="987" y1="470" x2="987" y2="1013"/>
    <line class="fold-line" x1="1258" y1="470" x2="1258" y2="1013"/>
    <line class="fold-line" x1="1530" y1="470" x2="1530" y2="1013"/>
    <line class="fold-line" x1="1010" y1="198" x2="1240" y2="198"/>
    <line class="fold-line" x1="1536" y1="1284" x2="1796" y2="1284"/>
  </g>

  <!-- Top tuck flap -->
  <g class="panel-top">
    <text class="brand-name" x="1065" y="346" font-size="50">QX Vita</text>
    <text class="brand-tag" x="1065" y="367" font-size="14">the lantern’s pick</text>
  </g>

  <!-- Side panel: story -->
  <g class="panel-story">
    <text class="sans navy" font-weight="700" font-size="22">
      <tspan x="743" y="570">the</tspan>
      <tspan x="743" y="593">lantern’s</tspan>
      <tspan x="743" y="616">pick</tspan>
    </text>
    <text class="italic grey" x="960" y="625" font-size="15" text-anchor="end">since XXXX</text>
    <line class="rule" x1="716" y1="629" x2="960" y2="629"/>
    <text class="script green" x="960" y="746" font-size="52" text-anchor="end">Life. Balanced.</text>
    <text class="italic grey" font-size="15" text-anchor="end">
      <tspan x="960" y="771">Lorem ipsum dolor sit amet,</tspan>
      <tspan x="960" y="789">consectetuer adipiscing elit, sed</tspan>
      <tspan x="960" y="808">diam nonummy nibh euismod</tspan>
      <tspan x="960" y="826">tincidunt ut laoreet dolore magna</tspan>
      <tspan x="960" y="844">aliquam erat volutpat. Ut wisi</tspan>
      <tspan x="960" y="863">enim ad minim veniam, quis</tspan>
    </text>
  </g>

  <!-- Front panel -->
  <g class="panel-front">
    <text class="brand-name" x="1013" y="558" font-size="50">QX Vita</text>
    <text class="brand-tag" x="1013" y="580" font-size="14">the lantern’s pick</text>
    <text class="product" x="1232" y="822" font-size="54" text-anchor="end"><tspan class="green" font-weight="600">Soft</tspan><tspan class="navy">Gels</tspan></text>
    <line class="rule" x1="1015" y1="828" x2="1372" y2="828"/>
    <text class="sans navy" x="1232" y="846" font-size="16" text-anchor="end">Pain Formulation</text>
    <text class="script white" x="1230" y="944" font-size="50" text-anchor="end">Life. Balanced.</text>
    <text class="sans white" x="1230" y="983" font-size="12" text-anchor="end">Content.</text>
  </g>

  <!-- Side panel: pain map -->
  <g class="panel-pain-map">
    <text class="sans white" font-weight="600" font-size="18">
      <tspan x="1286" y="511">Pain</tspan>
      <tspan x="1286" y="528">Formulation</tspan>
    </text>
    <text class="italic white" font-size="11">
      <tspan x="1286" y="546">our special formula helps to relieve</tspan>
      <tspan x="1286" y="560">different types of pain...</tspan>
    </text>
    <defs>
      <linearGradient id="anatomy-tones" x1="0" y1="0" x2="0" y2="1">
        <stop offset="0" stop-color="#ee8a5c"/>
        <stop offset="0.4" stop-color="#6aa4a6"/>
        <stop offset="0.7" stop-color="#8a58a8"/>
        <stop offset="1" stop-color="#d2508a"/>
      </linearGradient>
    </defs>
    <rect x="1290" y="574" width="210" height="412" rx="30" fill="url(#anatomy-tones)" opacity="0.75" role="img" aria-label="Colour anatomy illustration of the human muscular system, front view"/>
    <text class="sans navy" x="1423" y="622" font-size="11">contracture pain</text>
    <line class="rule" x1="1405" y1="627" x2="1530" y2="627" stroke-width="1.5"/>
    <text class="sans navy" x="1286" y="843" font-size="11">muscle pain</text>
    <text class="sans navy" x="1450" y="947" font-size="11">sprain pain</text>
    <line class="rule" x1="1410" y1="952" x2="1530" y2="952" stroke-width="1.5"/>
  </g>

  <!-- Back panel -->
  <g class="panel-back">
    <text class="product" x="1773" y="572" font-size="48" text-anchor="end"><tspan class="white" font-weight="600">Soft</tspan><tspan class="navy">Gels</tspan></text>
    <text class="sans navy" x="1773" y="595" font-size="15" text-anchor="end">Pain Formulation</text>
    <text class="sans green" x="1558" y="625" font-size="18" font-weight="600">Actives</text>
    <text class="italic navy" font-size="11">
      <tspan x="1558" y="639">Lorem ipsum Lorem ipsum</tspan>
      <tspan x="1558" y="653">dolor sit amet, consectetuer</tspan>
      <tspan x="1558" y="667">adipiscing elit, sed diam</tspan>
      <tspan x="1558" y="680">nonummy nibh euismod</tspan>
      <tspan x="1558" y="694">tincidunt ut laoreet dolore</tspan>
      <tspan x="1558" y="708">magna aliquam erat</tspan>
      <tspan x="1558" y="722">volutpat. Ut wisi enim ad</tspan>
      <tspan x="1558" y="736">minim veniam, quis nostrud</tspan>
    </text>
    <line class="rule" x1="1530" y1="753" x2="1775" y2="753"/>
    <text class="sans green" x="1558" y="778" font-size="18" font-weight="600">Medical Idications</text>
    <text class="italic navy" font-size="11">
      <tspan x="1558" y="793">Lorem ipsum Lorem ipsum</tspan>
      <tspan x="1558" y="807">dolor sit amet, consectetuer</tspan>
      <tspan x="1558" y="821">adipiscing elit, sed diam</tspan>
      <tspan x="1558" y="834">nonummy nibh euismod</tspan>
      <tspan x="1558" y="848">tincidunt ut laoreet dolore</tspan>
      <tspan x="1558" y="862">magna aliquam erat</tspan>
      <tspan x="1558" y="876">volutpat. Ut wisi enim ad</tspan>
      <tspan x="1558" y="890">minim veniam, quis nostrud</tspan>
    </text>
    <text class="brand-name" x="1557" y="976" font-size="40">QX Vita</text>
    <text class="brand-tag" x="1557" y="998" font-size="13">the lantern’s pick</text>
    <text class="italic navy" font-size="9" text-anchor="end">
      <tspan x="1773" y="936">Contact us at.</tspan>
      <tspan x="1773" y="947">xxxx@xxxxx.com</tspan>
      <tspan x="1773" y="959">000-0000-00</tspan>
      <tspan x="1773" y="970">Adress...</tspan>
    </text>
  </g>

  <!-- Bottom tuck panel -->
  <g class="panel-bottom">
    <text class="brand-name" x="1608" y="1168" font-size="50">QX Vita</text>
    <text class="brand-tag" x="1608" y="1190" font-size="14">the lantern’s pick</text>
  </g>
</svg>
</body>
</html>
```